New Website for Belcourt Manor at www.belcourt.com.au

A new logo has been designed (through pixel forge) and we now want to align the look and feel of our website at www.belcourt.com.au to the new logo. The content and page names (e.g. Grounds) will remain largely unchanged for the new site, so please submit a new look "Home" page, using our new logo, current text and any photos you choose from the existing gallery at our website. I have also attached the current "Home" page photos.

Industry/Entity Type

Accommodation

Number of Pages Required

1 page

Requirements
Must have
• Logo to be presented on white background.

```html
<!DOCTYPE html>
<html lang="en">
<head>
<meta charset="utf-8">
<title>Belcourt Manor – Home</title>
<link href="https://fonts.googleapis.com/css2?family=Lato:wght@300;400&family=Comic+Neue:wght@700&display=swap" rel="stylesheet">
<style>
:root{
  --brand:#0a9fe0;
  --brand-dark:#0a7fc0;
  --nav-grey:#8a8a8a;
  --body-grey:#5a5a5a;
  --caption:#3c3c3c;
  --white:#ffffff;
}
*{margin:0;padding:0;box-sizing:border-box}
html,body{width:960px;height:1200px;overflow:hidden;background:var(--white)}
body{position:relative;font-family:'Lato',sans-serif;font-weight:300}
.site-header{position:absolute;left:0;top:0;width:960px;height:84px;background:var(--white)}
.brand{position:absolute;left:46px;top:34px;display:flex;align-items:center;gap:8px;color:var(--brand-dark);font-size:24px;font-weight:400}
.brand-dot{width:14px;height:14px;border-radius:50%;background:#f6c21c}
.main-nav{position:absolute;left:306px;top:66px;display:flex;gap:10px;font-size:11.5px;color:var(--nav-grey);font-weight:400}
.main-nav .active{color:var(--brand)}
.hero{position:absolute;left:0;top:84px;width:960px;height:352px;background:linear-gradient(180deg,#d9e6f0 0%,#b9cfd9 25%,#5f7a47 60%,#3f5a2f 80%,#6a7c56 100%)}
.slider-dots{position:absolute;left:908px;top:142px;display:flex;flex-direction:column;gap:8px}
.slider-dots span{width:9px;height:9px;border-radius:50%;background:#c9c9c9}
.slider-dots .on{background:var(--brand)}
.hero-caption{position:absolute;left:0;top:264px;width:960px;height:88px;background:rgba(200,200,200,.9)}
.address{position:absolute;left:387px;top:8px;font-family:'Comic Neue',cursive;font-weight:700;font-size:23px;line-height:24px;color:var(--caption);letter-spacing:1px}
.hero-shadow{position:absolute;left:60px;top:436px;width:840px;height:12px;background:radial-gradient(ellipse at top,rgba(0,0,0,.28),rgba(0,0,0,0) 70%)}
.intro{position:absolute;left:0;top:453px;width:960px;height:228px;background:var(--brand);color:var(--white)}
.intro h1{font-weight:300;font-size:28px;text-align:center;margin-top:12px;letter-spacing:.3px}
.intro p{margin:6px 0 0 89px;width:790px;font-size:17px;line-height:22px}
.intro p + p{margin-top:8px}
.feature{position:absolute;top:694px;width:258px}
.feature h2{font-weight:300;font-size:18px;color:var(--brand);text-align:center;letter-spacing:.5px}
.feature .photo{display:block;width:258px;height:166px;margin-top:12px;box-shadow:0 3px 5px rgba(0,0,0,.25)}
.feature p{margin-top:12px;padding:0 2px;font-size:13px;line-height:16.3px;color:var(--body-grey);text-align:justify}
.f1{left:53px}.f2{left:345px}.f3{left:650px}
.f1 .photo{background:linear-gradient(180deg,#6f8a5c 0%,#d8a06a 40%,#c4653d 55%,#9b9585 100%)}
.f2 .photo{background:linear-gradient(180deg,#5e7b3e 0%,#c46a46 30%,#3f6a35 55%,#2f4f2a 100%)}
.f3 .photo{background:linear-gradient(90deg,#8a6a3a 0%,#e9e4dc 35%,#f1eee8 65%,#b07a52 100%)}
.site-footer{position:absolute;left:0;top:1144px;width:960px;height:56px;background:var(--brand);display:flex;justify-content:center;align-items:center;gap:12px;color:var(--white);font-size:13px;font-weight:400}
</style>
</head>
<body>
<header class="site-header">
  <div class="brand"><span class="brand-dot"></span>Belcourt Manor</div>
  <nav class="main-nav">
    <span class="active">Home</span><span>Mansion</span><span>Bedrooms</span><span>Options</span><span>Fox and Hare</span><span>Grounds</span><span>Location</span><span>Gallery</span><span>Contact</span><span>Availability</span><span>DIY Weddings</span>
  </nav>
</header>

<section class="hero" role="img" aria-label="Panorama of the manor house and landscaped gardens with palm trees">
  <div class="slider-dots"><span class="on"></span><span></span><span></span></div>
  <div class="hero-caption">
    <div class="address">42 Wrenfield Drive<br>Carrow,Gold Coast<br>Queenland,Australia</div>
  </div>
</section>
<div class="hero-shadow"></div>

<section class="intro">
  <h1>PALATIAL ESTATE AND LUXURY RESORT</h1>
  <p>On over 2 manicured garden acres, Belcourt Manor is a unique Gold Coast estate, centrally located in the prestigious rural suburb of Carrow.&nbsp; More about our Location</p>
  <p>The estate features a grand mansion, private pub (The Fox and Hare), sparkling resort pool, tennis court and playground.</p>
  <p>Magnificent properties rarely feel so warm and welcoming – so browse away and visit our photo gallery – and we look forward to having you stay as our guests.</p>
</section>

<article class="feature f1">
  <h2>MAIN HEADING</h2>
  <div class="photo" role="img" aria-label="Aerial view of the yellow manor with terracotta roofs and gravel driveway"></div>
  <p>Lorem Ipsum is simply dummy text of the printing and typesetting industry. Lorem Ipsum has been the industry's standard dummy text ever since the 1500s, when an unknown printer took a galley of type and scrambled it to make a type specimen book. It has survived not only five centuries, but also the leap into electronic typesetting, remaining essentially unchanged. It was popularised in the 1960s with the release of Transfer sheets containing Lorem Ipsum passages, and more recently with desktop publishing software like Quillset Layout including versions of Lorem Ipsum.</p>
</article>

<article class="feature f2">
  <h2>MAIN HEADING</h2>
  <div class="photo" role="img" aria-label="Aerial view of the resort pool surrounded by palms beside the manor"></div>
  <p>Lorem Ipsum is simply dummy text of the printing and typesetting industry. Lorem Ipsum has been the industry's standard dummy text ever since the 1500s, when an unknown printer took a galley of type and scrambled it to make a type specimen book. It has survived not only five centuries, but also the leap into electronic typesetting, remaining essentially unchanged. It was popularised in the 1960s with the release of Transfer sheets containing Lorem Ipsum passages, and more recently with desktop publishing software like Quillset Layout including versions of Lorem Ipsum.</p>
</article>

<article class="feature f3">
  <h2>MAIN HEADING</h2>
  <div class="photo" role="img" aria-label="Interior hallway with arches, framed paintings and a wrought iron balustrade"></div>
  <p>Lorem Ipsum is simply dummy text of the printing and typesetting industry. Lorem Ipsum has been the industry's standard dummy text ever since the 1500s, when an unknown printer took a galley of type and scrambled it to make a type specimen book. It has survived not only five centuries, but also the leap into electronic typesetting, remaining essentially unchanged. It was popularised in the 1960s with the release of Transfer sheets containing Lorem Ipsum passages, and more recently with desktop publishing software like Quillset Layout including versions of Lorem Ipsum.</p>
</article>

<footer class="site-footer">
  <span>Home Mansion</span><span>Bedrooms</span><span>Options</span><span>Fox and Hare</span><span>Grounds</span><span>Location</span><span>Gallery</span><span>Contact&nbsp; Availability DIY Weddings</span>
</footer>
</body>
</html>
```